Creative flyer for small business IT services

We are an IT services company based in Western Australia. We're looking to expand our market share amongst small businesses and need a brochure/flyer designed to give them a good overview of why we can help them. The design and layout should be consistent with an existing company profile brochure (included) but please be creative. A comprehensive brief with copy and a rough layout is included.

Small Business

```html
<!DOCTYPE html>
<html lang="en">
<head>
<meta charset="utf-8">
<title>Small Business IT Solutions – NorthGrid</title>
<link href="https://fonts.googleapis.com/css2?family=Source+Sans+3:wght@300;400;600;700&display=swap" rel="stylesheet">
<style>
:root{
  --red:#a01c22;
  --red-bright:#c8262c;
  --grey-box:#d9d9d9;
  --grey-bubble:#cfcfcf;
  --ink:#2b2b2b;
  --white:#ffffff;
  --soil:#6b4427;
  --leaf:#7fae3a;
}
*{box-sizing:border-box;margin:0;padding:0}
html,body{width:863px;height:1200px;overflow:hidden;background:#fff}
body{font-family:"Source Sans 3",Arial,sans-serif;color:var(--ink)}
.flyer{position:relative;width:863px;height:1200px;overflow:hidden;
  background:linear-gradient(180deg,#f4f4f4 0,#e6e6e6 22%,#ffffff 36%,#ffffff 100%)}
.abs{position:absolute}
.header-shapes,.footer-shapes{position:absolute;left:0;width:863px}
.header-shapes{top:0;height:215px}
.footer-shapes{top:1100px;height:100px}
.title{left:50px;top:44px;font-weight:300;font-size:38px;color:var(--white);letter-spacing:.2px}
.brand-mark{left:706px;top:40px;width:110px;height:108px;background:var(--white)}
.brand-name{left:690px;top:145px;width:140px;text-align:center;color:var(--white);font-size:21px;font-weight:400}
.bubble{left:43px;top:174px;width:386px;height:122px}
.bubble-text{left:64px;top:208px}
.bubble-text .big{font-weight:700;font-size:27px;color:#1f1f1f;line-height:1.1}
.bubble-text .sub{font-weight:300;font-size:23px;color:#1f1f1f;margin-top:4px}
.seedlings{left:60px;top:236px;width:776px;height:160px;
  background:linear-gradient(180deg,rgba(255,255,255,0) 0,rgba(127,174,58,.35) 45%,var(--soil) 82%,rgba(107,68,39,.2) 100%);
  clip-path:polygon(0 45%,44% 45%,44% 0,100% 0,100% 100%,0 100%)}
.rule{left:24px;top:411px;width:815px;height:1px;background:#333}
.lead{left:44px;top:419px;font-weight:400;font-size:25px;color:var(--red-bright)}
.intro{left:44px;top:458px;width:528px;font-size:13.2px;line-height:17px;font-weight:300;text-align:justify;color:#222}
.why{left:44px;top:526px;font-size:14.5px;color:var(--red-bright);font-weight:400}
.checks{left:44px;top:555px;list-style:none;font-size:13.5px;font-weight:300;color:#222}
.checks li{display:flex;align-items:center;height:22.7px}
.checks svg{margin-right:6px}
.faint-mark{left:469px;top:528px;width:92px;height:92px;background:#f5e3e3;opacity:.7}
.faint-name{left:452px;top:624px;width:128px;text-align:center;font-size:18px;color:#f1d7d7}
.panel{background:var(--grey-box)}
.audit{left:586px;top:432px;width:243px;height:172px;
  clip-path:polygon(0 0,93% 0,100% 9%,100% 100%,7% 100%,0 90%);padding:14px 16px}
.panel h3{font-size:16.5px;font-weight:700;color:var(--red-bright);margin-bottom:8px}
.panel p{font-size:10.4px;line-height:13.6px;font-weight:300;color:#222;text-align:justify;margin-bottom:12px}
.testimonials{left:644px;top:610px;width:185px;height:362px;
  clip-path:polygon(0 6%,8% 0,100% 0,100% 100%,0 100%);padding:10px 14px 0 14px}
.testimonials .who{font-weight:700;font-size:10.4px;color:#1f1f1f;margin:-4px 0 14px}
.testimonials .who.center{text-align:center}
.service{top:664px;width:195px;height:308px}
.service .body{position:absolute;left:0;top:24px;width:100%;height:284px;background:var(--grey-box);
  clip-path:polygon(0 0,100% 0,100% 92%,92% 100%,0 100%);padding:31px 9px 0 10px}
.service .tab{position:absolute;left:6px;top:0;width:172px;height:50px;background:var(--red);
  clip-path:polygon(0 52%,10% 0,100% 0,100% 60%,88% 100%,0 100%)}
.service .tab-title{position:absolute;left:32px;top:6px;font-size:15.5px;font-weight:700;color:#fff;line-height:18px}
.service .icon{position:absolute;left:120px;top:2px;width:46px;height:46px;border-radius:50%;
  background:radial-gradient(circle at 40% 35%,#9fd8ff,#1e74b8)}
.service p{font-size:10.6px;line-height:13.5px;font-weight:300;text-align:justify;color:#222;margin-bottom:13px}
.svc-1{left:36px}.svc-2{left:238px}.svc-3{left:446px}
.partners-h{left:44px;top:986px;font-size:16.5px;font-weight:700;color:var(--red)}
.partners-p{left:44px;top:1008px;width:430px;font-size:13.2px;line-height:17px;font-weight:300;text-align:justify}
.badge{background:#e7e7e7;border-radius:3px}
.b1{left:508px;top:992px;width:180px;height:26px;background:#eaf0f6}
.b2{left:509px;top:1030px;width:112px;height:44px;background:#1d3d63}
.b3{left:632px;top:1030px;width:48px;height:44px;background:#eef4fa;border:1px solid #d6dde5}
.b4{left:694px;top:992px;width:107px;height:55px;background:#f2f2f2;border:1px solid #d3d3d3;border-radius:5px}
.b4 .stripe{position:absolute;left:12px;top:14px;width:85px;height:12px;background:var(--red-bright)}
.join{left:360px;top:1084px;width:465px;text-align:right;font-size:13.5px;line-height:17px;font-weight:300;color:var(--red-bright)}
.foot-mark{left:51px;top:1147px;width:34px;height:34px;background:#fff}
.foot-name{left:93px;top:1150px;font-size:19px;color:#fff;font-weight:400}
.divider{top:1146px;width:1px;height:36px;background:#fff}
.foot-text{color:#fff;font-size:11px;line-height:14px;font-weight:400}
.addr{left:256px;top:1150px;text-align:center;display:flex;gap:3px}
.contact{left:470px;top:1150px;font-weight:400}
.contact div{display:flex;align-items:center;gap:4px}
.contact .web{font-weight:700}
.phone{left:664px;top:1150px;font-size:21px;font-weight:700;color:#fff;display:flex;align-items:center;gap:4px}
</style>
</head>
<body>
<main class="flyer">

  <svg class="header-shapes" viewBox="0 0 863 215" aria-hidden="true">
    <polygon points="0,0 863,0 863,176 0,122" fill="#a01c22"/>
    <polygon points="0,132 863,186 863,212 0,140" fill="#a01c22"/>
  </svg>

  <h1 class="abs title">Small Business IT Solutions</h1>
  <div class="abs brand-mark"></div>
  <div class="abs brand-name">NorthGrid</div>

  <svg class="abs bubble" viewBox="0 0 386 122" aria-hidden="true">
    <polygon points="0,0 386,0 340,98 70,98 58,118 40,98 0,98" fill="#cfcfcf"/>
  </svg>
  <div class="abs bubble-text">
    <div class="big">Small business. Big ideas.</div>
    <div class="sub">We’ll help your business grow.</div>
  </div>

  <div class="abs seedlings" role="img" aria-label="Row of six seedlings in mounds of soil, growing taller from left to right"></div>

  <div class="abs rule"></div>

  <h2 class="abs lead">We help small businesses get ahead of the pack.</h2>
  <p class="abs intro">You've always got more to do. In a small business, the last thing you need is another hat to wear. You shouldn't need to become a computer engineer to keep your business running smoothly. Say goodbye to IT headaches - our mission is to make your life easier.</p>

  <div class="abs faint-mark"></div>
  <div class="abs faint-name">NorthGrid</div>

  <h3 class="abs why">Here’s why small businesses love NorthGrid:</h3>
  <ul class="abs checks">
    <li><svg width="14" height="13" viewBox="0 0 14 13"><rect x="0.5" y="2.5" width="10" height="10" fill="none" stroke="#a01c22"/><path d="M2.5 7l3 3 7-9" fill="none" stroke="#a01c22" stroke-width="2"/></svg>We’re small business IT experts</li>
    <li><svg width="14" height="13" viewBox="0 0 14 13"><rect x="0.5" y="2.5" width="10" height="10" fill="none" stroke="#a01c22"/><path d="M2.5 7l3 3 7-9" fill="none" stroke="#a01c22" stroke-width="2"/></svg>We speak plain English and won’t waste your time</li>
    <li><svg width="14" height="13" viewBox="0 0 14 13"><rect x="0.5" y="2.5" width="10" height="10" fill="none" stroke="#a01c22"/><path d="M2.5 7l3 3 7-9" fill="none" stroke="#a01c22" stroke-width="2"/></svg>We care about our relationships</li>
    <li><svg width="14" height="13" viewBox="0 0 14 13"><rect x="0.5" y="2.5" width="10" height="10" fill="none" stroke="#a01c22"/><path d="M2.5 7l3 3 7-9" fill="none" stroke="#a01c22" stroke-width="2"/></svg>We worry about IT so you don’t have to</li>
  </ul>

  <section class="abs panel audit">
    <h3>Audit</h3>
    <p>It helps to know where you stand.</p>
    <p>Get a clearer picture of your IT systems with our obligation-free IT audit and consultation.</p>
    <p>Contact us today and we’ll provide you with expert insights into how your business can benefit from today’s amazing technology</p>
  </section>

  <section class="abs panel testimonials">
    <h3>Testimonials</h3>
    <p>Don’t just take our word for it! Here’s what some satisfied customers have to say about NorthGrid:</p>
    <p>“We are pleased to have NorthGrid as part of our team. I recommend NorthGrid for any business seeking a trustworthy, reliable and effective IT service provider.”</p>
    <div class="who">Mark Tully, Coastline Imaging</div>
    <p>“NorthGrid’s expertise has allowed us to test, analyse and improve the reliability and performance of our application, further improving the health and financial status of our business.”</p>
    <div class="who center">Peter Hollis, Ledger Path Pty Ltd</div>
  </section>

  <section class="abs service svc-1">
    <div class="body">
      <p>Say goodbye to IT interruptions, slow services, confusing jargon and inexplicable errors. We have solutions to your IT problems, and packages to suit every budget. We can even come to your workplace. If you run into a problem or need something done, just contact our Service Desk.</p>
      <p>Whether you have a single computer or a big team with complex requirements, our expert team can assist. We’ll give you an entire IT department for a fraction of the cost.</p>
    </div>
    <div class="tab"></div>
    <div class="tab-title">Support<br>Services</div>
    <div class="icon" role="img" aria-label="Support team icon"></div>
  </section>

  <section class="abs service svc-2">
    <div class="body">
      <p>Most of us insure our cars and homes, yet small businesses often don't protect themselves from the kind of disaster that strikes every day. Could your business recover from the complete loss of every electronic file - financial records, legal documents, customer information, intellectual property, archives, emails and more?</p>
      <p>Our Monitor &amp; Protect solutions keep you safe from physical threats like theft, fire and floods, but also from electronic threats like viruses and hackers. Best of all - it happens automatically, so you can relax.</p>
    </div>
    <div class="tab"></div>
    <div class="tab-title">Monitoring<br>&amp; Backup</div>
    <div class="icon" role="img" aria-label="Backup arrow icon"></div>
  </section>

  <section class="abs service svc-3">
    <div class="body">
      <p>Every business needs the right tools for the job. We supply world class hardware and software products from Brightsoft, Printwell, Corelane, Orchard, Netvale, Pixelform, Powerstay and many more. Our strong partnerships and buying power mean we can save you money.</p>
      <p>From a single keyboard to an entire infrastructure, we always take the time to help you select the right products.</p>
    </div>
    <div class="tab"></div>
    <div class="tab-title">Hardware &amp;<br>Software</div>
    <div class="icon" role="img" aria-label="Computer monitor and tools icon"></div>
  </section>

  <h3 class="abs partners-h">World Class Partnerships</h3>
  <p class="abs partners-p">We proudly work with a range of industry leaders to ensure your business is powered by the best of today’s technology. With major partners including Brightsoft, Corelane, Netvale, Virtura and Shieldpoint, you can be confident that our solutions are built on a strong foundation.</p>

  <div class="abs badge b1"></div>
  <div class="abs badge b2"></div>
  <div class="abs badge b3"></div>
  <div class="abs badge b4"><div class="stripe"></div></div>

  <p class="abs join">Our valued customers are already enjoying the benefits of partnering<br>with NorthGrid. Join them by contacting us today:</p>

  <svg class="footer-shapes" viewBox="0 0 863 100" aria-hidden="true">
    <polygon points="0,6 863,26 863,30 0,10" fill="#a01c22"/>
    <polygon points="0,14 863,34 863,100 0,100" fill="#a01c22"/>
  </svg>

  <div class="abs foot-mark"></div>
  <div class="abs foot-name">NorthGrid</div>
  <div class="abs divider" style="left:240px"></div>
  <div class="abs foot-text addr">
    <svg width="9" height="12" viewBox="0 0 9 12"><path d="M4.5 0a4.5 4.5 0 0 0-4.5 4.5C0 8 4.5 12 4.5 12S9 8 9 4.5A4.5 4.5 0 0 0 4.5 0zm0 6.2a1.7 1.7 0 1 1 0-3.4 1.7 1.7 0 0 1 0 3.4z" fill="#fff"/></svg>
    <div>Level 12, 80 Harbour Road<br>Perth WA 6000</div>
  </div>
  <div class="abs divider" style="left:436px"></div>
  <div class="abs foot-text contact">
    <div><svg width="12" height="9" viewBox="0 0 12 9"><rect x=".5" y=".5" width="11" height="8" fill="none" stroke="#fff"/><path d="M.5.5l5.5 4.5L11.5.5" fill="none" stroke="#fff"/></svg>sales@northgrid.com.au</div>
    <div class="web"><svg width="10" height="10" viewBox="0 0 10 10"><circle cx="5" cy="5" r="4.5" fill="none" stroke="#fff"/><ellipse cx="5" cy="5" rx="2" ry="4.5" fill="none" stroke="#fff"/><path d="M.5 5h9" stroke="#fff"/></svg>www.northgrid.com.au</div>
  </div>
  <div class="abs divider" style="left:646px"></div>
  <div class="abs phone">
    <svg width="18" height="18" viewBox="0 0 18 18"><circle cx="9" cy="9" r="8" fill="none" stroke="#fff" stroke-width="1.5"/><path d="M6.3 4.8l1.4 2-.8 1a6 6 0 0 0 2.9 2.9l1-.8 2 1.4-.6 1.6c-3.6-.2-7.3-3.900-7.5-7.5z" fill="#fff"/></svg>
    1300 555 019
  </div>

</main>
</body>
</html>
```